VaultMeridan Business Card Re-Design

VaultMeridan is a specialized information security company that applies its proven methodology of security Assessment, Development, Integration and Training (A-D-I-T) to provide cyber security services in the areas of Data Protection, Network Defense and Compliance. We need the current business card re-designed to properly scale the fonts and possibly rearranging some elements (icons, lettering, etc.) to make the card more appealing to the eye. The card should have the logo that is on the web site (www.vaultmeridan-example.com). We would like ideas for both a black card (black background) and a white card (white background). We prefer rounded corners to help the card stand out but are open to all ideas. FYI: VaultMeridan's slogan is "...Your defense is our mission".

Target Market(s)

#1 US Government Contracting Companies, #2 Commercial Companies, #3 Gen. Public.

Industry/Entity Type

Business

Contact Information for Business Card

See Description; open to the use of different fonts.

Font styles to use
Sans Serif

Colors
000000
ec1f27
ffffff

Requirements
Must have
• Company logo on web site, rounded corners, list of company offerings on the back of the card.
Nice to have
• Icons
Should not have
• none

```html
<!DOCTYPE html>
<html lang="en">
<head>
<meta charset="utf-8">
<title>VaultMeridan Business Card</title>
<link href="https://fonts.googleapis.com/css2?family=Open+Sans:wght@400;600&display=swap" rel="stylesheet">
<style>
  :root {
    --ink: #1a1a1a;
    --card-black: #262626;
    --red: #ec1f27;
    --white: #ffffff;
    --backdrop: #e8e5e1;
  }
  * { margin: 0; padding: 0; box-sizing: border-box; }
  html, body { width: 1200px; height: 1000px; overflow: hidden; }
  body {
    position: relative;
    background: var(--backdrop);
    font-family: "Open Sans", Arial, sans-serif;
  }
  .card {
    position: absolute;
    left: 265px;
    width: 665px;
    height: 397px;
    border-radius: 22px;
    overflow: hidden;
  }
  .card-front { top: 73px; background: var(--white); color: var(--ink); }
  .card-back { top: 533px; background: var(--card-black); color: var(--white); }

  .name-marker {
    position: absolute; left: 0; top: 99px; width: 8px; height: 41px;
    background: var(--red);
  }
  .person-name {
    position: absolute; left: 34px; top: 94px;
    font-size: 24px; font-weight: 600; line-height: 1.2;
  }
  .person-title {
    position: absolute; left: 33px; top: 125px;
    font-size: 16px; line-height: 1.3;
  }
  .contact-list { position: absolute; left: 33px; top: 170px; list-style: none; }
  .contact-item {
    display: flex; align-items: flex-start; gap: 7px;
    font-size: 16.5px; line-height: 22px; margin-bottom: 2px;
  }
  .contact-item.address { margin-bottom: 6px; }
  .contact-icon { width: 14px; height: 14px; margin-top: 4px; flex: none; fill: var(--red); }

  .brand-name {
    position: absolute; font-weight: 600; white-space: nowrap;
  }
  .card-front .brand-name { left: 385px; top: 248px; font-size: 30px; color: var(--ink); }

  .slogan-band {
    position: absolute; left: 0; bottom: 0; width: 100%; height: 38px;
    background: var(--red); color: var(--white);
    display: flex; align-items: center; justify-content: center;
    font-size: 16px; letter-spacing: 11.5px; text-transform: uppercase;
    padding-left: 11.5px;
  }

  .card-back .brand-name.header { left: 33px; top: 30px; font-size: 28px; color: var(--white); }
  .card-back .brand-name.feature { left: 370px; top: 170px; font-size: 38px; color: var(--white); }

  .services { position: absolute; left: 33px; top: 104px; list-style: none; }
  .service {
    font-size: 16.5px; line-height: 20.4px; white-space: nowrap;
  }
  .service::before {
    content: "•"; color: var(--red); margin-right: 5px;
  }
</style>
</head>
<body>
  <section class="card card-front">
    <span class="name-marker"></span>
    <h1 class="person-name">Marcus Hale</h1>
    <p class="person-title">President / CEO - CSSA, CNDP</p>
    <ul class="contact-list">
      <li class="contact-item address">
        <svg class="contact-icon" viewBox="0 0 14 14"><path d="M7 0a5 5 0 0 0-5 5c0 3.5 5 9 5 9s5-5.5 5-9a5 5 0 0 0-5-5zm0 7a2 2 0 1 1 0-4 2 2 0 0 1 0 4z"/></svg>
        <span>1420 Harbor Ridge Dr. Suite 210<br>Easton, Maryland 21601</span>
      </li>
      <li class="contact-item">
        <svg class="contact-icon" viewBox="0 0 14 14"><path d="M4 0h6a1 1 0 0 1 1 1v12a1 1 0 0 1-1 1H4a1 1 0 0 1-1-1V1a1 1 0 0 1 1-1zm.5 1.5v10h5v-10z"/></svg>
        <span>555.014.2201</span>
      </li>
      <li class="contact-item">
        <svg class="contact-icon" viewBox="0 0 14 14"><path d="M1 4c0-2 2-3 6-3s6 1 6 3v1H10V3.5H4V5H1zM3 6h8l2 7H1z"/></svg>
        <span>555.019.3627</span>
      </li>
      <li class="contact-item">
        <svg class="contact-icon" viewBox="0 0 14 14"><path d="M0 3h14v9H0zm1 1v.5l6 4 6-4V4z"/></svg>
        <span>info@vaultmeridan-example.com</span>
      </li>
      <li class="contact-item">
        <svg class="contact-icon" viewBox="0 0 14 14"><path d="M0 3h14v9H0zm1 1v.5l6 4 6-4V4z"/></svg>
        <span>mhale@vaultmeridan-example.com</span>
      </li>
      <li class="contact-item">
        <svg class="contact-icon" viewBox="0 0 14 14"><path d="M7 0a7 7 0 1 0 0 14A7 7 0 0 0 7 0zm0 1.5c.8 0 1.6 1.6 1.9 4.5H5.1C5.4 3.1 6.2 1.5 7 1.5zM5.1 8h3.8c-.3 2.9-1.1 4.5-1.9 4.5S5.4 10.9 5.1 8zM1.6 6a5.5 5.5 0 0 1 2.6-3.9C3.8 3.2 3.6 4.5 3.5 6zm0 2h1.9c.1 1.5.3 2.8.7 3.9A5.5 5.5 0 0 1 1.6 8zm8.9-2c-.1-1.5-.3-2.8-.7-3.9A5.5 5.5 0 0 1 12.4 6zm0 2h1.9a5.5 5.5 0 0 1-2.6 3.9c.4-1.1.6-2.4.7-3.9z"/></svg>
        <span>www.vaultmeridan-example.com</span>
      </li>
    </ul>
    <div class="brand-name">VaultMeridan</div>
    <div class="slogan-band">Your defense is our mission</div>
  </section>

  <section class="card card-back">
    <div class="brand-name header">VaultMeridan</div>
    <ul class="services">
      <li class="service">Secure Cloud &amp; Hybrid Stack Solutions</li>
      <li class="service">Network Attack Penetration &amp; Defense</li>
      <li class="service">Red/Blue Team</li>
      <li class="service">Data Center Consolidation</li>
      <li class="service">Secure Virtual Computing</li>
      <li class="service">Classified Cross Domian Solutions</li>
      <li class="service">Foreign/Counter Intelligence Date Security</li>
      <li class="service">Certification &amp; Accreditation</li>
      <li class="service">Secure Wireless Solutions</li>
      <li class="service">Security Training , Assessments &amp; Integration</li>
      <li class="service">Security Subject Matter Experts</li>
      <li class="service">Executive Security Strategy Coaching</li>
      <li class="service">Data Encryption/Privacy</li>
    </ul>
    <div class="brand-name feature">VaultMeridan</div>
  </section>
</body>
</html>
```